Poster for mountain bike and trail run competition

I am looking for a poster design for a charitable mountain bike and trail run race. It should be something fun, colorful, which can attract participants. The area in which the competition takes place is dominated by hills and by the Nera river which has a beautiful gorge.. I am attaching some of our previous (poorly designed) posters. The poster should have a place where I can add the sponsor logos, which I will do by myself, in the following months.
Text:
Headline: "Poiana Tulvei Mountain Bike and Trail Run Race"
small headline: "Editia a-6a"
small headline: "Valea Brelvei, 10-11 IUNIE 2023"
other text:
"10 IUNIE - Concurs Mountain Bike & Concert
11 IUNIE - Concurs Trail Run"
text for enrollments: "inscrieri pe www.brelvacros.ro"

Thanks

• a space where I can add sponsor logos, editable file to be provided (AI, photoshop or corel)

```html
<!DOCTYPE html>
<html lang="ro">
<head>
<meta charset="utf-8">
<title>Poiana Tulvei Mountain Bike and Trail Run Race – Poster</title>
<link rel="stylesheet" href="https://fonts.googleapis.com/css2?family=Rubik+Dirt&family=Roboto+Condensed:wght@700&family=Roboto:wght@700;900&display=swap">
<style>
  :root {
    --race-red: #e8202a;
    --ink: #0b0b0b;
    --paper: #ffffff;
    --backdrop: #e9eaec;
    --font-grunge: "Rubik Dirt", "Impact", sans-serif;
    --font-condensed: "Roboto Condensed", "Arial Narrow", sans-serif;
    --font-url: "Roboto", "Arial", sans-serif;
  }
  * { margin: 0; padding: 0; box-sizing: border-box; }
  html, body {
    width: 1200px; height: 1200px; overflow: hidden;
    background: var(--backdrop);
  }
  .poster {
    position: absolute; left: 198px; top: 30px;
    width: 804px; height: 1140px;
    background: var(--paper);
    overflow: hidden;
  }
  .poster__scene { position: absolute; left: 0; top: 0; width: 804px; height: 960px; display: block; }
  .poster__sponsors { position: absolute; left: 0; top: 960px; width: 804px; height: 180px; background: var(--paper); }

  .line { position: absolute; white-space: nowrap; line-height: 1; }
  .headline { font-family: var(--font-grunge), sans-serif; text-transform: uppercase; }
  .headline--red { color: var(--race-red); }
  .headline--white { color: var(--paper); }
  .headline__small { font-size: 0.62em; color: var(--paper); }

  .info { font-family: var(--font-condensed), sans-serif; font-weight: 700; text-transform: uppercase; }
  .info--red { color: var(--race-red); }
  .info--white { color: var(--paper); }

  .signup { font-family: var(--font-condensed), sans-serif; font-weight: 700; color: var(--paper); font-size: 30px; }
  .signup__url {
    font-family: var(--font-url), sans-serif; font-weight: 900;
    color: var(--race-red); font-size: 42px; letter-spacing: 4px;
    margin-left: 8px;
  }
</style>
</head>
<body>
<main class="poster">
  <svg class="poster__scene" viewBox="0 0 804 960" role="img"
       aria-label="Illustration: silhouette of a mountain biker seen from behind, rocky gorge peaks with pine trees and birds, a trail runner and a cyclist on a dark ridge">
    <defs>
      <linearGradient id="sceneTone" x1="0" y1="0" x2="1" y2="0.15">
        <stop offset="0" stop-color="#111111"/>
        <stop offset="0.48" stop-color="#1a0a0a"/>
        <stop offset="0.62" stop-color="#c81c24"/>
        <stop offset="1" stop-color="#e8202a"/>
      </linearGradient>
    </defs>
    <rect x="0" y="0" width="804" height="770" fill="url(#sceneTone)"/>
    <path d="M0 770 C 200 760, 400 775, 560 765 S 760 755, 804 760 L 804 960 L 0 960 Z" fill="#0b0b0b"/>
  </svg>

  <div class="line headline headline--red" style="left:141px; top:232px; font-size:72px;">Poiana</div>
  <div class="line headline headline--red" style="left:80px; top:296px; font-size:88px;">Tulvei</div>
  <div class="line headline headline--white" style="left:127px; top:400px; font-size:48px;">Mountain</div>
  <div class="line headline headline--red" style="left:127px; top:446px; font-size:60px;">Bike <span class="headline__small">and</span></div>
  <div class="line headline headline--red" style="left:127px; top:504px; font-size:66px;">Trail</div>
  <div class="line headline headline--white" style="left:109px; top:570px; font-size:84px;">Run Race</div>

  <div class="line info info--red" style="left:109px; top:666px; font-size:44px;">Editia a-6a</div>
  <div class="line info info--white" style="left:109px; top:724px; font-size:32px;">Valea Brelvei,</div>
  <div class="line info info--white" style="left:109px; top:758px; font-size:26px;">10-11 iunie 2023</div>

  <div class="line info info--white" style="left:372px; top:718px; font-size:22px;">10 iunie</div>
  <div class="line info info--white" style="left:372px; top:746px; font-size:22px;">Concurs mountain bike</div>
  <div class="line info info--white" style="left:372px; top:776px; font-size:22px;">&amp; concert</div>
  <div class="line info info--red" style="left:372px; top:816px; font-size:22px;">11 iunie</div>
  <div class="line info info--red" style="left:372px; top:845px; font-size:22px;">Concurs trail run</div>

  <div class="line signup" style="left:109px; top:893px;">inscrieri pe<span class="signup__url">www.brelvacros.ro</span></div>

  <section class="poster__sponsors" aria-label="Sponsor area"></section>
</main>
</body>
</html>
```